Snuggle Stitch Needs a Beautiful Website

I need a new website for this new E-commerce. I sell handmade baby crochets, e.g. booties, headbands, hats, etc. I need a feminine and soft design to make the moms-to-be say 'oohh ahh'. I'd like pink, blue and gray. I'd like an inviting homepage, and nice regular pages where people can see and order the products.

Industry/Entity Type

Baby

Requirements
Must have
• beautiful, soft, feminine design. Please use pictures of the colors I'd like: brown, yellow, pink and blue. Any combination, but definitely include brown.

```html
<!DOCTYPE html>
<html lang="en">
<head>
<meta charset="utf-8">
<title>Snuggle Stitch – Handmade Baby Crochet</title>
<link rel="stylesheet" href="https://fonts.googleapis.com/css2?family=Source+Sans+3:ital,wght@0,300;0,400;0,600;1,700&family=Arimo:wght@400;700&display=swap">
<style>
  :root {
    --page-bg: #ececec;
    --sheet-bg: #f5f5f5;
    --pink: #d9366f;
    --crimson: #c8093d;
    --teal: #35b3d1;
    --text: #333333;
    --muted: #666666;
    --line: #dddddd;
    --white: #ffffff;
    --sale: #4aa520;
  }
  * { box-sizing: border-box; margin: 0; padding: 0; }
  html, body { width: 1200px; height: 1000px; overflow: hidden; }
  body { background: var(--page-bg); font-family: "Arimo", Arial, sans-serif; color: var(--text); position: relative; }
  .sheet { position: absolute; left: 100px; top: 0; width: 1020px; height: 1000px; background: var(--sheet-bg); }
  .abs { position: absolute; white-space: nowrap; }

  /* header */
  .brand { left: 270px; top: 32px; font-family: "Source Sans 3", sans-serif; font-weight: 600; font-size: 27px; line-height: 34px; color: var(--pink); display: flex; align-items: center; gap: 8px; }
  .brand-dot { width: 12px; height: 12px; border-radius: 50%; background: var(--teal); }
  .top-links { top: 13px; font-size: 9px; color: #444; }
  .top-links.cart { left: 704px; display: flex; align-items: center; gap: 5px; }
  .top-links.checkout { left: 826px; }
  .top-links.account { left: 888px; color: var(--crimson); display: flex; align-items: center; gap: 5px; }
  .top-links.sep { color: #bbb; }
  .login-label { left: 499px; top: 50px; font-size: 9px; font-weight: 700; color: #333; }
  .field { top: 45px; height: 21px; width: 121px; background: var(--white); border: 1px solid #d6d6d6; font-size: 8.5px; color: #888; padding: 5px 7px; }
  .field.email { left: 537px; }
  .field.password { left: 667px; }
  .field .forgot { position: absolute; right: 7px; top: 5px; color: var(--crimson); }
  .btn { top: 44px; height: 22px; background: var(--pink); color: var(--white); font-size: 9.5px; display: flex; align-items: center; justify-content: center; }
  .btn.login { left: 797px; width: 50px; }
  .btn.guest { left: 857px; width: 100px; }

  .nav-item { top: 98px; font-family: "Source Sans 3", sans-serif; font-weight: 300; font-size: 14.5px; color: #444; }
  .nav-item .plus { margin-left: 5px; font-size: 11px; }
  .search { left: 837px; top: 97px; width: 120px; height: 21px; background: var(--white); border: 1px solid #d6d6d6; font-size: 8.5px; color: #999; display: flex; align-items: center; gap: 6px; padding-left: 7px; }

  /* hero */
  .hero { left: 100px; top: 130px; width: 1020px; height: 353px; background: radial-gradient(ellipse at 55% 45%, #b9e7f0 0%, #9fdbe8 18%, #e3e4e4 42%, #dedfdf 100%); }
  .hero-title { left: 263px; top: 345px; width: 478px; height: 52px; background: rgba(53,179,209,.92); color: var(--white); font-family: "Source Sans 3", sans-serif; font-weight: 300; font-size: 26px; line-height: 32px; padding: 8px 13px; }
  .hero-text { left: 263px; top: 399px; width: 404px; height: 46px; background: rgba(53,179,209,.92); color: var(--white); font-size: 9px; line-height: 15px; padding: 8px 15px; white-space: normal; }
  .hero-text .more { position: absolute; right: 10px; bottom: 8px; font-weight: 700; font-size: 10px; }
  .pager { left: 566px; top: 475px; display: flex; gap: 7px; }
  .pager span { width: 17px; height: 17px; border-radius: 50%; border: 2px solid var(--crimson); background: var(--white); color: var(--crimson); font-size: 8px; font-weight: 700; display: flex; align-items: center; justify-content: center; }
  .pager span.active { background: var(--crimson); color: var(--white); }

  /* intro */
  .intro-frame { left: 265px; top: 507px; width: 175px; height: 176px; background: var(--white); box-shadow: 0 0 3px rgba(0,0,0,.15); padding: 5px; }
  .intro-frame div { width: 100%; height: 100%; background: linear-gradient(160deg, #777 0%, #3a3a3a 55%, #d8d8d8 100%); }
  .intro-title { left: 473px; top: 510px; font-family: "Source Sans 3", sans-serif; font-style: italic; font-weight: 700; font-size: 14px; color: var(--crimson); }
  .intro-copy { left: 476px; top: 538px; width: 484px; font-size: 8.6px; line-height: 15px; color: #444; white-space: normal; }
  .intro-copy strong { display: block; font-size: 9.5px; color: #222; }
  .intro-copy p { margin-bottom: 15px; }

  /* featured */
  .section-head { left: 262px; top: 700px; font-family: "Source Sans 3", sans-serif; font-weight: 300; font-size: 17px; color: #444; }
  .view-more { left: 879px; top: 708px; font-size: 8px; color: #444; display: flex; align-items: center; gap: 6px; }
  .section-rule { left: 262px; top: 730px; width: 695px; height: 1px; background: var(--line); }
  .card { top: 755px; width: 160px; height: 245px; background: var(--white); box-shadow: 0 0 3px rgba(0,0,0,.12); padding: 6px; text-align: center; }
  .card .photo { height: 184px; }
  .card .name { margin-top: 7px; font-family: "Source Sans 3", sans-serif; font-weight: 300; font-size: 10.5px; color: #555; }
  .card .price { margin-top: 2px; font-family: "Source Sans 3", sans-serif; font-size: 16px; color: var(--crimson); }
  .card .price s { font-size: 11px; color: #999; margin-left: 4px; }
  .sale-tag { left: 438px; top: 752px; }
</style>
</head>
<body>
  <div class="sheet"></div>

  <header>
    <div class="abs brand"><span>Snuggle Stitch</span><span class="brand-dot"></span></div>
    <div class="abs top-links cart">
      <svg width="12" height="10" viewBox="0 0 12 10"><path d="M0 1h2l2 6h6l1.5-4.5H3" fill="none" stroke="#333" stroke-width="1.2"/><circle cx="5" cy="9" r="1" fill="#333"/><circle cx="9" cy="9" r="1" fill="#333"/></svg>
      <span>0 items ($0.00 in total)</span>
    </div>
    <div class="abs top-links sep" style="left:815px">|</div>
    <div class="abs top-links checkout">Checkout</div>
    <div class="abs top-links sep" style="left:874px">|</div>
    <div class="abs top-links account"><svg width="10" height="10" viewBox="0 0 10 10"><circle cx="5" cy="3" r="2.5" fill="#c8093d"/><path d="M0 10c0-3 2-4.5 5-4.5s5 1.5 5 4.5z" fill="#c8093d"/></svg>My account ^</div>
    <div class="abs login-label">Log-in:</div>
    <div class="abs field email">E-mail address</div>
    <div class="abs field password">Password<span class="forgot">Forget?</span></div>
    <div class="abs btn login">Log-in</div>
    <div class="abs btn guest">Continue as guest</div>

    <nav>
      <span class="abs nav-item" style="left:263px">Home</span>
      <span class="abs nav-item" style="left:323px">Catagories<span class="plus">+</span></span>
      <span class="abs nav-item" style="left:421px">Products<span class="plus">+</span></span>
      <span class="abs nav-item" style="left:509px">Blog</span>
      <span class="abs nav-item" style="left:560px">Features</span>
      <span class="abs nav-item" style="left:645px">Contact</span>
    </nav>
    <div class="abs search">
      <svg width="11" height="11" viewBox="0 0 11 11"><circle cx="4.5" cy="4.5" r="3.5" fill="none" stroke="#222" stroke-width="1.6"/><path d="M7 7l3.5 3.5" stroke="#222" stroke-width="1.8"/></svg>
      <span>search here</span>
    </div>
  </header>

  <section>
    <div class="abs hero" role="img" aria-label="Photo of a light blue crocheted baby crown headband"></div>
    <h1 class="abs hero-title">Lorem ipsum dolor sit amet consectetur</h1>
    <div class="abs hero-text">Lorem ipsum dolor sit amet, consectetur adipiscing elit. Mauris eu fringilla odio, nec luctus ipsum, Mauris eu fringilla odio, nec luctus ipsum.<span class="more">Read more +</span></div>
    <div class="abs pager"><span>1</span><span class="active">2</span><span>3</span><span>4</span></div>
  </section>

  <section>
    <div class="abs intro-frame"><div role="img" aria-label="Photo of black and white crocheted baby sneakers"></div></div>
    <h2 class="abs intro-title">Snuggle Stitch</h2>
    <div class="abs intro-copy">
      <strong>Welcome !!</strong>
      <p>Lorem ipsum dolor sit amet, consectetur adipiscing elit. Mauris eu fringilla odio, nec luctus ipsum. Proin sit amet ipsum sem. Duis feugiat, sapien sit amet aliquet volutpat, nisi ligula suscipit sem, convallis viverra diam tortor fringilla turpis. Phasellus vel condimentum eros. Sed nisi est, porta eget sagittis in, ultrices ac lacus. Morbi fermentum vestibulum lacus fringilla luctus. Aenean orci neque.</p>
      <p>Lorem ipsum dolor sit amet, consectetur adipiscing elit. Mauris eu fringilla odio, nec luctus ipsum. Proin sit amet ipsum sem. Duis feugiat, sapien sit amet aliquet volutpat, nisi ligula suscipit sem, convallis viverra diam tortor fringilla turpis. Phasellus vel condimentum eros. Sed nisi est, porta eget sagittis in, ultrices ac lacus. Morbi fermentum vestibulum lacus fringilla luctus. Aenean orci neque.</p>
    </div>
  </section>

  <section>
    <h2 class="abs section-head">Featured items</h2>
    <div class="abs view-more">
      <svg width="12" height="8" viewBox="0 0 12 8"><path d="M0 4C2 0.5 10 0.5 12 4C10 7.5 2 7.5 0 4z" fill="#333"/><circle cx="6" cy="4" r="1.6" fill="#fff"/></svg>
      <span>view more items</span>
    </div>
    <div class="abs section-rule"></div>

    <article class="abs card" style="left:263px">
      <div class="photo" role="img" aria-label="Photo of pink crocheted baby booties with flowers" style="background:linear-gradient(170deg,#f2c7d8 0%,#e88aa6 55%,#e3dcdc 100%)"></div>
      <div class="name">Striped colorfull dress</div>
      <div class="price">$39.99</div>
    </article>
    <article class="abs card" style="left:441px">
      <div class="photo" role="img" aria-label="Photo of a bright pink crocheted crown headband" style="background:radial-gradient(ellipse at 50% 50%,#e657c8 0%,#ee8bd8 35%,#eeeeee 75%)"></div>
      <div class="name">Polka dot light blue blouse</div>
      <div class="price">$19.99<s>$36.99</s></div>
    </article>
    <article class="abs card" style="left:619px">
      <div class="photo" role="img" aria-label="Photo of brown crocheted baby sneakers with a pink star" style="background:linear-gradient(165deg,#a85b8e 0%,#5e4c44 40%,#3e3430 70%,#cfcfcf 100%)"></div>
      <div class="name">Basic sleeveless sweater</div>
      <div class="price">$29.99</div>
    </article>
    <article class="abs card" style="left:797px">
      <div class="photo" role="img" aria-label="Photo of a soft pink crocheted crown headband" style="background:radial-gradient(ellipse at 50% 55%,#f47fb0 0%,#f3a6c6 35%,#d8d5da 75%)"></div>
      <div class="name">Colorful summer dress</div>
      <div class="price">$24.99</div>
    </article>

    <svg class="abs sale-tag" width="50" height="50" viewBox="0 0 50 50" aria-label="Sale">
      <path d="M0 20L20 0H48L0 48z" fill="var(--sale)"/>
      <text x="17" y="27" transform="rotate(-45 17 27)" fill="#fff" font-family="Arimo, sans-serif" font-size="11">sale</text>
    </svg>
  </section>
</body>
</html>
```